Business Card Design

We need a business card design for a new company located in Lindenfield, NV, entitled 'BrightPath Chiropractic & Holistic Center'. Our services include restoration of health and vitality, spinal exam, health assessment, dietary & fitness programs, lymphatic & therapeutic massage, detox & remineralize body wraps, far infrared sauna therapy

Industry/Entity Type

Business

Contact Information for Business Card

BrightPath Chiropractic & Holistic Center, Marlena Oskow LMT, 4512 Hwy. 9, Suite 310, Lindenfield, NV 77381, 702-555-0193

```html
<!DOCTYPE html>
<html lang="en">
<head>
<meta charset="utf-8">
<title>BrightPath Chiropractic &amp; Holistic Center – Business Card</title>
<link rel="stylesheet" href="https://fonts.googleapis.com/css2?family=Source+Sans+3:wght@400;600&display=swap">
<style>
  :root {
    --page: #e4e4e4;
    --card: #030303;
    --teal: #1aa18a;
    --brand-blue: #1f6c9e;
    --label-blue: #1a9ad6;
    --brand-grey: #707070;
    --white: #ffffff;
    --font: "Source Sans 3", "Myriad Pro", Arial, sans-serif;
  }
  * { box-sizing: border-box; margin: 0; padding: 0; }
  html, body {
    width: 1189px; height: 1200px; overflow: hidden;
    background: var(--page);
    font-family: var(--font);
  }
  .card {
    position: absolute; left: 140px;
    width: 918px; height: 523px;
    background: var(--card);
    box-shadow: 0 6px 14px rgba(0,0,0,.35);
    overflow: hidden;
  }
  .card--front { top: 46px; }
  .card--back { top: 624px; }
  .card > * { position: absolute; }
  .curves { left: 0; top: 0; width: 918px; height: 523px; }

  .brand-mark { left: 190px; top: 50px; width: 120px; height: 120px; border-radius: 50%; background: var(--brand-blue); }
  .brand-name { left: 394px; top: 78px; color: var(--brand-grey); font-weight: 400; line-height: 1; }
  .brand-name__main { display: block; font-size: 48px; }
  .brand-name__sub { display: block; font-size: 25px; margin-top: 4px; letter-spacing: 1.4px; }

  .person { left: 0; width: 918px; text-align: center; top: 232px; }
  .person__name { color: var(--brand-blue); font-size: 52px; line-height: 1; font-weight: 400; }
  .person__title { color: var(--white); font-size: 29px; line-height: 1.1; }

  .contact { color: var(--white); font-size: 29px; line-height: 1; white-space: nowrap; }
  .contact__label { position: absolute; color: var(--label-blue); font-size: 31px; }
  .phone { top: 358px; left: 0; width: 918px; height: 32px; }
  .web-mail { top: 408px; left: 0; width: 918px; height: 32px; }
  .contact__value { position: absolute; }
  .address { left: 0; width: 918px; top: 458px; text-align: center; color: var(--white); font-size: 29px; white-space: nowrap; }

  .services-mark { left: 26px; top: 64px; width: 84px; height: 84px; border-radius: 50%; background: var(--brand-blue); }
  .services-rule { left: 104px; right: 0; top: 109px; height: 3px; background: var(--teal); }
  .services-title { left: 149px; top: 52px; color: var(--label-blue); font-size: 62px; line-height: 1; font-weight: 400; }
  .service-list { left: 214px; top: 146px; list-style: none; }
  .service-list li {
    position: relative; padding-left: 54px;
    color: var(--white); font-size: 30px; height: 49px; line-height: 40px;
  }
  .service-list li::before {
    content: ""; position: absolute; left: 6px; top: 12px;
    width: 16px; height: 16px; border-radius: 50%; background: var(--white);
  }
</style>
</head>
<body>

<section class="card card--front">
  <svg class="curves" viewBox="0 0 918 523" aria-hidden="true">
    <path d="M0 162 Q440 292 918 146" fill="none" stroke="var(--teal)" stroke-width="3"/>
    <path d="M0 398 Q440 262 918 410" fill="none" stroke="var(--teal)" stroke-width="3"/>
  </svg>

  <div class="brand-mark" aria-hidden="true"></div>
  <h1 class="brand-name">
    <span class="brand-name__main">BrightPath</span>
    <span class="brand-name__sub">Chiropractic &amp; Holistic Center</span>
  </h1>

  <div class="person">
    <p class="person__name">Daniel Reyes</p>
    <p class="person__title">President</p>
  </div>

  <div class="contact phone">
    <span class="contact__label" style="left:337px;top:-2px">T:</span>
    <span class="contact__value" style="left:392px">702-555-0193</span>
  </div>
  <div class="contact web-mail">
    <span class="contact__label" style="left:74px;top:-2px">W :</span>
    <span class="contact__value" style="left:151px">www.brightpathhc.com</span>
    <span class="contact__label" style="left:477px;top:-2px">E :</span>
    <span class="contact__value" style="left:541px">care@brightpathhc.com</span>
  </div>
  <p class="address">Marlena Oskow LMT, 4512 Hwy. 9, Suite 310, Lindenfield, NV 77381</p>
</section>

<section class="card card--back">
  <div class="services-rule" aria-hidden="true"></div>
  <div class="services-mark" aria-hidden="true"></div>
  <h2 class="services-title">services</h2>
  <ul class="service-list">
    <li>dietary &amp; fitness programs</li>
    <li>lymphatic &amp; therapeutic massage</li>
    <li>spinal exam</li>
    <li>health assessment</li>
    <li>far infrared sauna therapy</li>
    <li>restoration of health and vitality</li>
    <li>detox &amp; remineralize body wraps</li>
  </ul>
</section>

</body>
</html>
```